2019 Chase the Morning Comet (Cardio Calendar)

I would like to put together a calendar of cardio workouts for the year. I would have 4 different workouts per week + 2 basic steady state workouts. I envision a picture of me on the top page and along with the challenge of the month description and the 3 different types of cardio description. on the bottom page would be the calendar for that month with the workout typed into the box. I am not sure if a boxed calendar would be enough space to write each workout in so I am open to more ideas on how to present the workouts

Target Market(s)

Women 20-60 years old
moms
couples
men
athletes

Industry/Entity Type

Fitness

Font styles to use
Sans Serif

Colors

Designer to choose colors to be used in the design.

Requirements
Must have
• Ability to incorporate 4 different workouts per week in a downloadable calendar style
• I want to have a different picture available for each month
• modern, bold, but simple and clean presentation
Nice to have
• picture at the top, with a description of the 3 different types of workouts for that month.
• On the bottom would be space for separate days of each workout
Should not have
• NA

```html
<!DOCTYPE html>
<html lang="en">
<head>
<meta charset="utf-8">
<title>2019 Chase the Morning Comet – January</title>
<link href="https://fonts.googleapis.com/css2?family=Cinzel:wght@400;700&family=Roboto+Condensed:wght@400&display=swap" rel="stylesheet">
<style>
  :root{
    --backdrop:#ecebe8;
    --paper:#ffffff;
    --red:#d5143a;
    --navy:#1b2a41;
    --ink:#1d2433;
    --rule:#4a5160;
    --sun-tint:#f6d3cc;
    --sat-tint:#d6d6db;
    --muted:#9a9aa2;
    --sun-muted:#ee9e90;
  }
  *{box-sizing:border-box;margin:0;padding:0}
  html,body{width:1200px;height:800px;overflow:hidden}
  body{background:var(--backdrop);position:relative;font-family:"Roboto Condensed",Arial,sans-serif}
  .calendar-page{position:absolute;left:345px;top:5px;width:510px;height:790px;background:var(--paper);box-shadow:0 2px 10px rgba(0,0,0,.12);overflow:hidden}
  .hero-photo{position:absolute;left:0;top:0;width:510px;height:300px;
    background:linear-gradient(180deg,#06080d 0%,#0d1422 55%,#173019 78%,#2c6b2a 100%)}
  .hero-swoosh{position:absolute;left:0;top:280px;width:510px;height:50px}
  .month-title{position:absolute;left:12px;top:318px;font-family:"Cinzel",Georgia,serif}
  .month-title .year{display:block;font-size:20px;color:var(--ink);line-height:1}
  .month-title .month{display:block;font-size:38px;font-weight:700;color:var(--red);line-height:1;letter-spacing:-1px}
  .month-grid{position:absolute;left:12px;top:389px;width:490px;display:grid;
    grid-template-columns:repeat(7,1fr);grid-template-rows:20px repeat(5,52px)}
  .day-head{font-family:"Cinzel",Georgia,serif;font-weight:700;font-size:12px;color:var(--ink);
    text-align:center;line-height:20px;border-left:1px solid var(--rule)}
  .day-head:first-child{border-left:none}
  .sun{background:var(--sun-tint)}
  .sat{background:var(--sat-tint)}
  .day-head.sun{color:var(--red)}
  .day{position:relative;border-left:1px solid var(--rule);border-top:1px solid var(--rule);padding:9px 3px 0 4px}
  .day.sun{border-left:none}
  .date{position:absolute;right:4px;top:5px;font-family:"Cinzel",Georgia,serif;font-weight:700;font-size:13px;color:var(--ink)}
  .sun .date{color:var(--red)}
  .day.other .date{color:var(--muted);font-weight:400}
  .day.sun.other .date{color:var(--sun-muted)}
  .workouts{list-style:none;font-size:6.2px;line-height:8.2px;color:var(--ink)}
  .workouts li::before{content:"2";color:var(--red);margin-right:1px}
  .photo-slots{position:absolute;left:12px;top:680px;width:490px;height:100px;display:grid;grid-template-columns:repeat(3,1fr);gap:12px}
  .photo-slot{background:var(--navy)}
</style>
</head>
<body>
<main class="calendar-page">
  <div class="hero-photo" role="img" aria-label="Photo of an athlete in red leggings stretching with a foam roller on turf at night"></div>
  <svg class="hero-swoosh" viewBox="0 0 510 50" aria-hidden="true">
    <polygon points="0,20 510,4 510,20 70,27 0,27" fill="var(--red)"/>
    <polygon points="0,27 70,27 510,20 510,24 82,27" fill="var(--paper)"/>
    <polygon points="82,28 510,23 510,42 115,44" fill="var(--navy)"/>
  </svg>

  <h1 class="month-title"><span class="year">2019</span><span class="month">JANUARY</span></h1>

  <section class="month-grid">
    <div class="day-head sun">SUN</div><div class="day-head">MON</div><div class="day-head">TUE</div><div class="day-head">WED</div><div class="day-head">THU</div><div class="day-head">FRI</div><div class="day-head sat">SAT</div>

    <div class="day sun other"><span class="date">30</span></div>
    <div class="day other"><span class="date">31</span></div>
    <div class="day"><span class="date">1</span><ul class="workouts"><li>Lorem Ipsum</li><li>Lorem Ipsum</li><li>Lorem Ipsum</li></ul></div>
    <div class="day"><span class="date">2</span><ul class="workouts"><li>Lorem Ipsum</li><li>Lorem Ipsum</li></ul></div>
    <div class="day"><span class="date">3</span><ul class="workouts"><li>Lorem Ipsum</li><li>Lorem Ipsum</li><li>Lorem Ipsum</li><li>Lorem Ipsum</li></ul></div>
    <div class="day"><span class="date">4</span><ul class="workouts"><li>Lorem Ipsum</li><li>Lorem Ipsum</li><li>Lorem Ipsum</li><li>Lorem Ipsum</li></ul></div>
    <div class="day sat"><span class="date">5</span><ul class="workouts"><li>Lorem Ipsum</li><li>Lorem Ipsum</li><li>Lorem Ipsum</li><li>Lorem Ipsum</li></ul></div>

    <div class="day sun"><span class="date">6</span></div>
    <div class="day"><span class="date">7</span><ul class="workouts"><li>Lorem Ipsum</li><li>Lorem Ipsum</li></ul></div>
    <div class="day"><span class="date">8</span><ul class="workouts"><li>Lorem Ipsum</li></ul></div>
    <div class="day"><span class="date">9</span><ul class="workouts"><li>Lorem Ipsum</li><li>Lorem Ipsum</li></ul></div>
    <div class="day"><span class="date">10</span><ul class="workouts"><li>Lorem Ipsum</li><li>Lorem Ipsum</li><li>Lorem Ipsum</li></ul></div>
    <div class="day"><span class="date">11</span><ul class="workouts"><li>Lorem Ipsum</li><li>Lorem Ipsum</li><li>Lorem Ipsum</li><li>Lorem Ipsum</li></ul></div>
    <div class="day sat"><span class="date">12</span><ul class="workouts"><li>Lorem Ipsum</li><li>Lorem Ipsum</li><li>Lorem Ipsum</li><li>Lorem Ipsum</li></ul></div>

    <div class="day sun"><span class="date">13</span></div>
    <div class="day"><span class="date">14</span><ul class="workouts"><li>Lorem Ipsum</li></ul></div>
    <div class="day"><span class="date">15</span><ul class="workouts"><li>Lorem Ipsum</li><li>Lorem Ipsum</li><li>Lorem Ipsum</li></ul></div>
    <div class="day"><span class="date">16</span><ul class="workouts"><li>Lorem Ipsum</li><li>Lorem Ipsum</li></ul></div>
    <div class="day"><span class="date">17</span><ul class="workouts"><li>Lorem Ipsum</li><li>Lorem Ipsum</li><li>Lorem Ipsum</li><li>Lorem Ipsum</li></ul></div>
    <div class="day"><span class="date">18</span><ul class="workouts"><li>Lorem Ipsum</li><li>Lorem Ipsum</li></ul></div>
    <div class="day sat"><span class="date">19</span><ul class="workouts"><li>Lorem Ipsum</li><li>Lorem Ipsum</li><li>Lorem Ipsum</li></ul></div>

    <div class="day sun"><span class="date">20</span></div>
    <div class="day"><span class="date">21</span><ul class="workouts"><li>Lorem Ipsum</li><li>Lorem Ipsum</li><li>Lorem Ipsum</li></ul></div>
    <div class="day"><span class="date">22</span><ul class="workouts"><li>Lorem Ipsum</li><li>Lorem Ipsum</li></ul></div>
    <div class="day"><span class="date">23</span><ul class="workouts"><li>Lorem Ipsum</li><li>Lorem Ipsum</li></ul></div>
    <div class="day"><span class="date">24</span><ul class="workouts"><li>Lorem Ipsum</li></ul></div>
    <div class="day"><span class="date">25</span><ul class="workouts"><li>Lorem Ipsum</li><li>Lorem Ipsum</li><li>Lorem Ipsum</li><li>Lorem Ipsum</li></ul></div>
    <div class="day sat"><span class="date">26</span><ul class="workouts"><li>Lorem Ipsum</li><li>Lorem Ipsum</li></ul></div>

    <div class="day sun"><span class="date">27</span></div>
    <div class="day"><span class="date">28</span><ul class="workouts"><li>Lorem Ipsum</li></ul></div>
    <div class="day"><span class="date">29</span><ul class="workouts"><li>Lorem Ipsum</li><li>Lorem Ipsum</li><li>Lorem Ipsum</li></ul></div>
    <div class="day"><span class="date">30</span><ul class="workouts"><li>Lorem Ipsum</li><li>Lorem Ipsum</li><li>Lorem Ipsum</li></ul></div>
    <div class="day"><span class="date">31</span><ul class="workouts"><li>Lorem Ipsum</li><li>Lorem Ipsum</li></ul></div>
    <div class="day other"><span class="date">1</span></div>
    <div class="day sat other"><span class="date">2</span></div>
  </section>

  <section class="photo-slots">
    <div class="photo-slot" role="img" aria-label="Space for workout photo one"></div>
    <div class="photo-slot" role="img" aria-label="Space for workout photo two"></div>
    <div class="photo-slot" role="img" aria-label="Space for workout photo three"></div>
  </section>
</main>
</body>
</html>
```